modern real estate design
business card/letterhead/envelop
Dorian Parks
President
408 W Birch Avenue Belle Plaine, MN 56093
dorian@tidewaterhomesgroup.com
www.tidewaterhomesgroup.com
Licensed Realtor with Quiet Harbor Real Estate
Escape Gravity.
newell343 newell343
I am also interested in getting a design done for metal business cards. It would be cool to have them die cut, etched, and have our two color logo on them. Thanks.

```html
<!DOCTYPE html>
<html lang="en">
<head>
<meta charset="utf-8">
<title>Tidewater Homes Group – Business Card</title>
<link rel="stylesheet" href="https://fonts.googleapis.com/css2?family=Montserrat:wght@400;500;700&display=swap">
<style>
  :root {
    --backdrop: #e4e5e7;
    --card: #ffffff;
    --ink: #4a4f56;
    --ink-soft: #7b8088;
    --teal: #45b3c1;
    --edge-band: #5d6168;
  }
  * { box-sizing: border-box; margin: 0; padding: 0; }
  html, body {
    width: 1200px; height: 883px; overflow: hidden;
    background: var(--backdrop);
    font-family: "Montserrat", sans-serif;
    color: var(--ink);
  }
  .canvas {
    position: relative; width: 1200px; height: 883px;
  }
  .card {
    position: absolute; left: 325px;
    width: 550px; height: 314px;
    background: var(--card);
    border-radius: 22px;
    box-shadow: 0 10px 28px rgba(0,0,0,0.12);
    overflow: hidden;
  }
  .card--front { top: 95px; }
  .card--back { top: 474px; }

  .brand {
    display: flex; align-items: center; gap: 12px;
  }
  .brand__dot {
    width: 26px; height: 26px; border-radius: 50%;
    background: var(--teal);
  }
  .brand__name {
    font-weight: 700; letter-spacing: 0.08em;
    text-transform: uppercase; color: var(--ink);
    line-height: 1.15;
  }
  .card--front .brand {
    position: absolute; left: 50%; top: 50%;
    transform: translate(-50%, -50%);
  }
  .card--front .brand__name { font-size: 27px; }
  .card--front .brand__dot { width: 40px; height: 40px; }

  .edge-band {
    position: absolute; left: 0; top: 78px;
    width: 10px; height: 150px;
    background: var(--edge-band);
  }
  .card--back .brand {
    position: absolute; right: 36px; top: 48px;
  }
  .card--back .brand__name { font-size: 18px; }

  .contact {
    position: absolute; left: 38px; top: 84px;
  }
  .contact__name {
    font-size: 15px; font-weight: 700; letter-spacing: 0.06em;
    text-transform: uppercase;
  }
  .contact__title {
    font-size: 11px; color: var(--ink-soft); margin-top: 3px;
  }
  .contact__list {
    list-style: none; margin-top: 26px;
    display: flex; flex-direction: column; gap: 8px;
  }
  .contact__item {
    display: flex; align-items: center; gap: 9px;
    font-size: 10.5px; color: var(--ink);
  }
  .contact__icon { width: 12px; height: 12px; flex: none; }

  .address {
    position: absolute; right: 36px; top: 160px;
    text-align: left; font-size: 11px; line-height: 1.6;
    color: var(--ink);
  }
</style>
</head>
<body>
<main class="canvas">

  <section class="card card--front" aria-label="Card front">
    <div class="brand">
      <span class="brand__dot"></span>
      <span class="brand__name">Tidewater<br>Homes Group</span>
    </div>
  </section>

  <section class="card card--back" aria-label="Card back">
    <div class="edge-band"></div>

    <div class="contact">
      <p class="contact__name">Dorian Parks</p>
      <p class="contact__title">President</p>
      <ul class="contact__list">
        <li class="contact__item">
          <svg class="contact__icon" viewBox="0 0 24 24" fill="var(--teal)"><path d="M6.6 10.8a15.1 15.1 0 0 0 6.6 6.6l2.2-2.2a1 1 0 0 1 1-.25 11.4 11.4 0 0 0 3.6.57 1 1 0 0 1 1 1V20a1 1 0 0 1-1 1A17 17 0 0 1 3 4a1 1 0 0 1 1-1h3.5a1 1 0 0 1 1 1c0 1.25.2 2.45.57 3.57a1 1 0 0 1-.25 1z"/></svg>
          555 014 2290
        </li>
        <li class="contact__item">
          <svg class="contact__icon" viewBox="0 0 24 24" fill="var(--teal)"><path d="M6.6 10.8a15.1 15.1 0 0 0 6.6 6.6l2.2-2.2a1 1 0 0 1 1-.25 11.4 11.4 0 0 0 3.6.57 1 1 0 0 1 1 1V20a1 1 0 0 1-1 1A17 17 0 0 1 3 4a1 1 0 0 1 1-1h3.5a1 1 0 0 1 1 1c0 1.25.2 2.45.57 3.57a1 1 0 0 1-.25 1z"/></svg>
          555 014 2291
        </li>
        <li class="contact__item">
          <svg class="contact__icon" viewBox="0 0 24 24" fill="var(--teal)"><path d="M6.6 10.8a15.1 15.1 0 0 0 6.6 6.6l2.2-2.2a1 1 0 0 1 1-.25 11.4 11.4 0 0 0 3.6.57 1 1 0 0 1 1 1V20a1 1 0 0 1-1 1A17 17 0 0 1 3 4a1 1 0 0 1 1-1h3.5a1 1 0 0 1 1 1c0 1.25.2 2.45.57 3.57a1 1 0 0 1-.25 1z"/></svg>
          555 014 2292
        </li>
        <li class="contact__item">
          <svg class="contact__icon" viewBox="0 0 24 24" fill="var(--teal)"><path d="M2 5h20v14H2z M2 5l10 8 10-8" stroke="#fff" stroke-width="1.6"/></svg>
          dorian@tidewaterhomesgroup.com
        </li>
        <li class="contact__item">
          <svg class="contact__icon" viewBox="0 0 24 24" fill="none" stroke="var(--teal)" stroke-width="2.2"><circle cx="12" cy="12" r="10"/><path d="M2 12h20M12 2c3 3 3 17 0 20M12 2c-3 3-3 17 0 20"/></svg>
          www.tidewaterhomesgroup.com
        </li>
      </ul>
    </div>

    <div class="brand">
      <span class="brand__dot"></span>
      <span class="brand__name">Tidewater<br>Homes Group</span>
    </div>

    <address class="address" style="font-style:normal">
      408 W Birch Avenue<br>
      Belle Plaine, MN 56093
    </address>
  </section>

</main>
</body>
</html>
```